Help Design the Packaging for our Nicotine Replacement Therapy

Packaging Design Brief for Brevora
We are using this contest to find a designer who can design the packaging for the full line of products listed below for our new brand. This contest will require you to provide designs for the Traditional mint in both the 2mg and 4mg, and the Traditional Cinnamon 2 mg and 4mg, plus the mint in the Modern, 2mg and 4mg. We would like to see how you propose to tie the designs together so their is clear differentiate between the products and flavors, yet it maintains brand cohesiveness.
We would like to then work with the contest winner on a 1-1 project to develop the packaging for the remaining products.
Project Overview:
Brevora is launching a new line of nicotine replacement therapy (NRT) products, including gum and lozenges in multiple flavors and strengths. The packaging design needs to reflect Brevora’s brand values of trust, warmth, professionalism, and customer-centricity while being visually appealing, functional, and easily distinguishable.
Here is our full product line up so you can design product packaging that has the potential to expand as we add more flavors.
Product Line-Up:
1. Nicotine Gum ("Traditional" because it tastes and feels like hollbeck's gum):
- Flavors: Mint, Fruit, Cinnamon
- Strengths: 2mg, 4mg
- Pack Size: 240 pieces per pack
2. Nicotine Gum (Stiffer, Playdough-Like Texture will be called "Classic"):
- Strengths: 2mg, 4mg
3. Nicotine Lozenges:
- Flavors: Mint, Citrus, Berry
- Strengths: 2mg, 4mg
- Pack Size: 120 pieces per pack
Design Objectives:
1. Brand Consistency:
- The Brevora logo should be easily recognizable across all packaging.
- The design should reflect the brand’s personality: trustworthy, professional, warm, and approachable.
- Packaging should evoke a sense of reliability and comfort, appealing to a mature audience.
2. Differentiation:
- Flavor Differentiation:
- Use distinct colors for each flavor to ensure they are easily distinguishable.
- Incorporate icons or images that represent the flavor (e.g., mint leaves for Mint, cinnamon sticks for Cinnamon).
- Strength Differentiation:
- Clearly display the nicotine strength (2mg or 4mg) in a way that stands out at a glance.
- Gum Texture Differentiation:
- Create a visual distinction between the traditional chewing gum and the stiffer, playdough-like gum while maintaining a cohesive brand look.
- Consider using different background textures, patterns, or additional design elements to indicate the different textures while ensuring they still feel part of the same family.
3. Product Type Differentiation:
- Gum vs. Lozenges:
- The lozenges should be visually distinct from the gum products while still fitting within the overall Brevora brand aesthetic.
- Consider using a different shape or design element on the lozenge packaging (e.g., a lozenge icon or a unique pattern) to differentiate them from the gum.
- Maintain consistent use of colors for flavors across both gum and lozenge packaging (e.g., Mint gum and Mint lozenges should share the same color scheme) to unify the product line.
4. Scalability:
- The design should be flexible enough to accommodate additional flavors or product variations in the future.
- Ensure that any new flavor or product type can be easily integrated into the existing design template.
Content Requirements:
1. Front of Pack:
- Brevora logo
- Flavor name and representative image
- Nicotine strength (2mg or 4mg)
- Indication of gum type (Traditional or Stiffer texture)
- Pack size (e.g., "240 Pieces")
2. Here are the die lines from the manufacturer. You will see that there are certain things that must be included on the gum packaging:
https://files.tarnowbox.net/folders/8qpe27Lm_X4v81ZsKd0n-WRyTa3GbU7Hc?usp=share_link
Overall Feel:
- The packaging should communicate that Brevora is a trustworthy, professional brand with a warm, supportive approach. It should feel modern and appeal to a broad audience both male and female.
Packaging design for all SKUs listed above, with clear differentiation between flavors, strengths, and product types.
Here is the link to the brevora logo. https://files.tarnowbox.net/file/d/7-RHbwPqJmm412LcuvzxAq3QWEtn5ZK9S/view?usp=sharing We are not opposed to the color of the dots and + sign changing to signify flavor either.
Target Market(s)
individuals 18-55+ looking to quit vaping and smoking
Industry/Entity Type
nicotine replacement therapy
Other font styles liked:
- should compliment and look good with our logo and font which is Nexa bold
Requirements
Must have
- we want to look professional and trustworthy. . .and we want a design that is cohesive across the product set and can expand and stay on brand with additional flavors.
Nice to have
- We will pick a winner and then pay that winner to do the rest of the package designs for each sku and lozenges too.

```html
<!DOCTYPE html>
<html lang="en">
<head>
<meta charset="utf-8">
<title>Brevora Nicotine Gum and Lozenges – Packaging Fronts</title>
<link rel="stylesheet" href="https://fonts.googleapis.com/css2?family=Montserrat:wght@400;700&family=Roboto+Condensed:wght@700&family=Tinos:wght@700&display=swap">
<style>
  :root{
    --cinnamon:#c8610a;
    --fruits:#9a5fa8;
    --mint:#4db36b;
    --ink:#0b0b0b;
    --paper:#ffffff;
    --text:#f4f4f4;
    --sans:"Montserrat", sans-serif;
    --serif:"Tinos", serif;
    --cond:"Roboto Condensed", sans-serif;
  }
  *{box-sizing:border-box;margin:0;padding:0}
  html,body{width:1200px;height:882px;overflow:hidden;background:var(--paper)}
  .canvas{position:relative;width:1200px;height:882px}

  .pack{position:absolute;width:178px;height:280px;background:var(--ink);color:var(--text);overflow:hidden}
  .pack.cinnamon{--accent:var(--cinnamon)}
  .pack.fruits{--accent:var(--fruits)}
  .pack.mint{--accent:var(--mint)}
  .pack::before{content:"";position:absolute;inset:0;
    background:radial-gradient(ellipse 90% 50% at 70% 62%, color-mix(in srgb,var(--accent) 28%,transparent), transparent 70%)}
  .pack.lozenge-box::after,.label::after{content:"";position:absolute;left:0;right:0;top:0;height:70px;
    background:linear-gradient(var(--accent),transparent);opacity:.9}
  .label::after{height:48px;top:0}
  .pack > *{position:absolute;z-index:1}

  .classic-tab{top:0;left:50%;transform:translateX(-50%);background:var(--accent);color:var(--ink);
    font:700 10px/1 var(--sans);letter-spacing:.5px;padding:4px 9px;border-radius:0 0 3px 3px}
  .brand{top:34px;left:12px;display:flex;align-items:center;gap:5px;font:700 32px/1 var(--sans);color:var(--paper);letter-spacing:-.5px}
  .brand .dot{width:8px;height:8px;border-radius:50%;background:var(--accent)}
  .product-line{top:80px;left:12px;right:0;display:flex;align-items:center;gap:5px;
    font:400 11px/1 var(--sans);letter-spacing:1.2px;color:var(--accent);white-space:nowrap}
  .product-line .rule{flex:1;height:7px;background:var(--accent)}
  .strength{top:104px;left:13px;text-align:center;color:var(--accent)}
  .strength .num{display:block;font:700 32px/1 var(--sans)}
  .strength .unit{display:block;font:700 15px/1 var(--serif)}
  .coated{top:122px;right:10px;text-align:right;font:700 8.5px/1.1 var(--serif);text-transform:uppercase}
  .flavour{top:160px;right:0;width:92px;padding:3px 6px;background:var(--accent);text-align:right;
    font:700 13px/1 var(--serif);letter-spacing:.5px;color:var(--text)}
  .usage{top:166px;left:13px;font:700 7.4px/1.12 var(--cond);text-transform:uppercase;white-space:nowrap}
  .flavour-art{right:8px;bottom:34px;width:82px;height:52px;border-radius:40% 40% 12px 12px}
  .cinnamon .flavour-art{background:linear-gradient(135deg,#6a3412,#d9dcd6 70%)}
  .fruits .flavour-art{background:linear-gradient(135deg,#f08a1c,#c8352a 45%,#d9dcd6 80%)}
  .mint .flavour-art{background:linear-gradient(135deg,#3e9a3a,#d9dcd6 70%)}
  .count{left:13px;bottom:32px;display:flex;align-items:center;gap:3px;background:var(--accent);padding:3px 5px}
  .count .qty{font:700 16px/1 var(--serif)}
  .count .unit{font:700 5.5px/1.2 var(--serif);text-transform:uppercase}

  .label{width:150px;height:300px;background:linear-gradient(90deg,#1a1a1a,#3a3a3a 45%,#1c1c1c)}
  .label .brand{top:50px;left:10px;font-size:27px}
  .label .product-line{top:86px;left:10px;font-size:9.6px;letter-spacing:.8px}
  .label .strength{top:110px;left:12px}
  .label .strength .num{font-size:40px}
  .label .strength .unit{font-size:17px}
  .label .usage{top:112px;left:62px;font-size:9px;line-height:1.2}
  .label .flavour-art{right:26px;bottom:74px;width:84px;height:44px}
  .label .count{left:auto;right:10px;bottom:40px}
</style>
</head>
<body>
<main class="canvas">

  <!-- Gum boxes -->
  <section class="pack gum-box cinnamon" style="left:30px;top:36px">
    <div class="brand"><span class="dot"></span>Brevora</div>
    <div class="product-line">NICOTINE GUM <span class="rule"></span></div>
    <div class="strength"><span class="num">4</span><span class="unit">mg</span></div>
    <div class="coated">Coated<br>for bold<br>flavour</div>
    <div class="flavour">CINNAMON</div>
    <div class="usage">For those who<br>smoke their<br>first cigarette<br>more than 30<br>minutes after<br>waking up</div>
    <div class="flavour-art" role="img" aria-label="Cinnamon sticks beside two gum pieces"></div>
    <div class="count"><span class="qty">240</span><span class="unit">Pieces<br>4mg each</span></div>
  </section>

  <section class="pack gum-box fruits" style="left:218px;top:36px">
    <div class="brand"><span class="dot"></span>Brevora</div>
    <div class="product-line">NICOTINE GUM <span class="rule"></span></div>
    <div class="strength"><span class="num">4</span><span class="unit">mg</span></div>
    <div class="coated">Coated<br>for bold<br>flavour</div>
    <div class="flavour">FRUITS</div>
    <div class="usage">For those who<br>smoke their<br>first cigarette<br>more than 30<br>minutes after<br>waking up</div>
    <div class="flavour-art" role="img" aria-label="Orange, kiwi and berries on gum pieces"></div>
    <div class="count"><span class="qty">240</span><span class="unit">Pieces<br>4mg each</span></div>
  </section>

  <section class="pack gum-box mint" style="left:406px;top:36px">
    <div class="classic-tab">CLASSIC</div>
    <div class="brand"><span class="dot"></span>Brevora</div>
    <div class="product-line">NICOTINE GUM <span class="rule"></span></div>
    <div class="strength"><span class="num">4</span><span class="unit">mg</span></div>
    <div class="coated">Coated<br>for bold<br>flavour</div>
    <div class="flavour">MINT</div>
    <div class="usage">For those who<br>smoke their<br>first cigarette<br>more than 30<br>minutes after<br>waking up</div>
    <div class="flavour-art" role="img" aria-label="Mint leaves beside two gum pieces"></div>
    <div class="count"><span class="qty">240</span><span class="unit">Pieces<br>4mg each</span></div>
  </section>

  <!-- Lozenge boxes -->
  <section class="pack lozenge-box cinnamon" style="left:634px;top:36px">
    <div class="brand"><span class="dot"></span>Brevora</div>
    <div class="product-line">NICOTINE LOZENGES</div>
    <div class="strength"><span class="num">4</span><span class="unit">mg</span></div>
    <div class="coated">Coated<br>for bold<br>flavour</div>
    <div class="flavour">CINNAMON</div>
    <div class="usage">For those who<br>smoke their<br>first cigarette<br>more than 30<br>minutes after<br>waking up</div>
    <div class="flavour-art" role="img" aria-label="Cinnamon sticks beside round lozenges"></div>
    <div class="count"><span class="qty">120</span><span class="unit">Pieces<br>4mg each</span></div>
  </section>

  <section class="pack lozenge-box fruits" style="left:822px;top:36px">
    <div class="brand"><span class="dot"></span>Brevora</div>
    <div class="product-line">NICOTINE LOZENGES</div>
    <div class="strength"><span class="num">4</span><span class="unit">mg</span></div>
    <div class="coated">Coated<br>for bold<br>flavour</div>
    <div class="flavour">FRUITS</div>
    <div class="usage">For those who<br>smoke their<br>first cigarette<br>more than 30<br>minutes after<br>waking up</div>
    <div class="flavour-art" role="img" aria-label="Orange, kiwi and berries on round lozenges"></div>
    <div class="count"><span class="qty">120</span><span class="unit">Pieces<br>4mg each</span></div>
  </section>

  <section class="pack lozenge-box mint" style="left:1010px;top:36px">
    <div class="brand"><span class="dot"></span>Brevora</div>
    <div class="product-line">NICOTINE LOZENGES</div>
    <div class="strength"><span class="num">4</span><span class="unit">mg</span></div>
    <div class="coated">Coated<br>for bold<br>flavour</div>
    <div class="flavour">MINT</div>
    <div class="usage">For those who<br>smoke their<br>first cigarette<br>more than 30<br>minutes after<br>waking up</div>
    <div class="flavour-art" role="img" aria-label="Mint leaves beside round lozenges"></div>
    <div class="count"><span class="qty">120</span><span class="unit">Pieces<br>4mg each</span></div>
  </section>

  <!-- Lozenge bottle labels -->
  <section class="pack label mint" style="left:275px;top:548px">
    <div class="classic-tab">CLASSIC</div>
    <div class="brand"><span class="dot"></span>Brevora</div>
    <div class="product-line">NICOTINE LOZENGES</div>
    <div class="strength"><span class="num">2</span><span class="unit">mg</span></div>
    <div class="usage">For those who<br>smoke their<br>first cigarette<br>more than 30<br>minutes after<br>waking up</div>
    <div class="flavour-art" role="img" aria-label="Mint leaves beside round lozenges"></div>
    <div class="count"><span class="qty">120</span><span class="unit">Pieces<br>4mg each</span></div>
  </section>

  <section class="pack label cinnamon" style="left:465px;top:548px">
    <div class="brand"><span class="dot"></span>Brevora</div>
    <div class="product-line">NICOTINE LOZENGES</div>
    <div class="strength"><span class="num">2</span><span class="unit">mg</span></div>
    <div class="usage">For those who<br>smoke their<br>first cigarette<br>more than 30<br>minutes after<br>waking up</div>
    <div class="flavour-art" role="img" aria-label="Cinnamon sticks beside round lozenges"></div>
    <div class="count"><span class="qty">120</span><span class="unit">Pieces<br>4mg each</span></div>
  </section>

  <section class="pack label fruits" style="left:655px;top:548px">
    <div class="brand"><span class="dot"></span>Brevora</div>
    <div class="product-line">NICOTINE LOZENGES</div>
    <div class="strength"><span class="num">2</span><span class="unit">mg</span></div>
    <div class="usage">For those who<br>smoke their<br>first cigarette<br>more than 30<br>minutes after<br>waking up</div>
    <div class="flavour-art" role="img" aria-label="Orange, kiwi and berries on round lozenges"></div>
    <div class="count"><span class="qty">120</span><span class="unit">Pieces<br>4mg each</span></div>
  </section>

</main>
</body>
</html>
```